Sunvale Ride Co Splashpage

This webpage will be a holding page until our website is complete. This page needs to be designed to advertise our tours in Honolulu, Hawaii. So it is important to have prices displayed and have a Hawaiian theme.

1. Warm colors - suggest reds?
2. Hawaiian flower incorporated in design

3. Display prices
Adult - single Journey - $20
Adult - 1 Day - $20 (this needs to be displayed as a special deal/price because full price is $25)
Adult - 2 days - $30

Seniors - (62+) 1 Day + 1 Day Free - $20

Children 5 - 17 yrs - 1 Day - $13
Children 5 - 17 yrs - 2 Days - $15
Under 5 Yrs - Free

There will be an online booking button (text on button should say "Book Online", so please make sure it is clear where they can purchase the tickets.

3. A photo of our branded double decker bus should be incorporate on the page.

4. Our Message "Welcome to Sunvale Ride Co. Our Open Top Bus ensures you have an unrivalled view of Honolulu and all that this great city has to offer. We pass all of the city’s main sites, offering fantastic photo opportunities along the way. Our tour takes around 90 minutes. You can get on and off the bus as often as you want. Your ticket is valid for one or two days. All departures have commentary in English. If it’s raining, we have a sliding roof to keep you dry. Step on-board and let us show you the best of Honolulu."

5. Some tour sites our tour visits are: Marlow's Arcade, Waikiki beach, Umerik Palace, Bretoma Palace/King statue, Darvin's statue

We are catering to an international adult audience (ranging from 25 - 60 yrs of age) that handles vacation planning.

Please visit www.ridebyloop.ee to get an idea of our style.

• 1. prices displayed where they be viewed easily - There will be an online booking button so please make sure it is clear where they can purchase the tickets.

2. Adult - 1 Day - $20 (this needs to be displayed as a special deal/price because full price is $25)

3. Photo of our double decker bus

4. Hawaiian flower incorporated in design

5. Bright colors (make sure orange isn't the main background color) but not overwhelming

6. Logo on webpage
• 1. Images of our tour sites
2. Other Hawaiian images such as palm trees, Maile Lei, Sun with sunglasses, flower lei, parrot, Hawaiian sunsets
• -Do not want any shade of orange as the main background color

```html
<!DOCTYPE html>
<html lang="en">
<head>
<meta charset="utf-8">
<title>Sunvale Ride Co – Tour Prices</title>
<link rel="stylesheet" href="https://fonts.googleapis.com/css2?family=Source+Sans+3:wght@300;400;700;900&display=swap">
<style>
  :root {
    --ink: #222222;
    --navy: #14186e;
    --muted: #9a9488;
    --strike: #d2332b;
    --paper: #ede6d7;
    --paper-edge: #e3dac7;
    --frame: #fbfbf8;
    --title: #f3df1b;
    --btn-top: #fff36a;
    --btn-bottom: #f1d000;
    --btn-edge: #d2b400;
    --stone-light: #e9e6e0;
    --stone-dark: #a9a49b;
  }
  * { margin: 0; padding: 0; box-sizing: border-box; }
  html, body { width: 1200px; height: 750px; overflow: hidden; }
  body { font-family: "Source Sans 3", Arial, sans-serif; color: var(--ink); }

  .page {
    position: relative; width: 1200px; height: 750px; overflow: hidden;
    background: radial-gradient(ellipse at 30% 30%, var(--stone-light), #cfcac1 55%, var(--stone-dark));
  }
  .backdrop { position: absolute; inset: 0;
    background:
      radial-gradient(circle at 8% 75%, rgba(255,255,255,.55), transparent 18%),
      radial-gradient(circle at 92% 30%, rgba(255,255,255,.45), transparent 15%),
      radial-gradient(circle at 75% 90%, rgba(120,115,105,.35), transparent 20%),
      radial-gradient(circle at 45% 12%, rgba(255,255,255,.4), transparent 22%);
  }

  .price-sheet {
    position: absolute; left: 190px; top: 190px; width: 820px; height: 560px;
    background: linear-gradient(180deg, var(--paper), var(--paper-edge));
    box-shadow: 0 0 18px rgba(0,0,0,.18);
  }

  .brand {
    position: absolute; left: 135px; top: 62px;
    font-weight: 900; font-size: 54px; letter-spacing: 2px;
    text-transform: uppercase; color: var(--title); line-height: 1;
  }

  .snapshot {
    position: absolute; background: var(--frame); padding: 9px;
    box-shadow: 3px 4px 10px rgba(0,0,0,.35);
  }
  .snapshot .fill { width: 100%; height: 100%; }
  .snap-tower { left: -10px; top: 132px; width: 200px; height: 250px; transform: rotate(-6deg); }
  .snap-tower .fill { background: linear-gradient(180deg, #2f74c9, #6fa6de 55%, #e9ecef 56%, #c9ccd0 80%, #2e4a28); }
  .snap-bus { left: 678px; top: -18px; width: 418px; height: 275px; transform: rotate(5deg); }
  .snap-bus .fill { background: linear-gradient(180deg, #6f7f5e 0%, #c9242c 30%, #b51f27 58%, #3f6a2c 72%, #5c9134); }
  .snap-statue { left: 945px; top: 350px; width: 265px; height: 290px; transform: rotate(4deg); }
  .snap-statue .fill { background: linear-gradient(160deg, #d9ece0, #6c8a58 40%, #6e4f35 65%, #4a3324); }

  .label { position: absolute; line-height: 1.3; font-weight: 400; white-space: nowrap; }
  .label small { display: block; font-size: 15px; }
  .label span { display: block; font-size: 18px; text-transform: uppercase; }

  .price { position: absolute; font-weight: 300; font-size: 48px; line-height: 1; letter-spacing: -2px; white-space: nowrap; }
  .price.deal { font-weight: 700; color: var(--navy); }
  .price.navy { color: var(--navy); }
  .was {
    position: absolute; font-weight: 300; font-size: 25px; color: var(--muted); letter-spacing: -1px;
    text-decoration: line-through; text-decoration-color: var(--strike);
  }
  .free { position: absolute; font-weight: 900; font-size: 46px; color: var(--navy); letter-spacing: -1px; line-height: 1; }

  .tag {
    position: absolute; display: flex; align-items: center; justify-content: center;
    border: 1.5px solid var(--navy); border-radius: 50%; white-space: nowrap;
    font-weight: 900; font-size: 14px; color: var(--navy); text-transform: uppercase; letter-spacing: -.5px;
  }

  .book-online {
    position: absolute; left: 410px; top: 570px; width: 340px; height: 80px;
    border-radius: 14px; border: 2px solid var(--btn-edge);
    background: linear-gradient(180deg, var(--btn-top), var(--btn-bottom));
    box-shadow: 0 3px 6px rgba(0,0,0,.3);
    display: flex; align-items: center; justify-content: center;
    font-weight: 700; font-size: 44px; letter-spacing: -1.5px; color: var(--navy); text-decoration: none;
  }
</style>
</head>
<body>
<div class="page">
  <div class="backdrop" role="img" aria-label="Soft blurred photo of smooth white pebbles"></div>

  <div class="price-sheet"></div>

  <div class="snapshot snap-tower"><div class="fill" role="img" aria-label="Photo of a white clock tower against a blue sky with palm trees"></div></div>
  <div class="snapshot snap-bus"><div class="fill" role="img" aria-label="Photo of the red Sunvale Ride Co open-top double-decker bus parked by a lawn"></div></div>
  <div class="snapshot snap-statue"><div class="fill" role="img" aria-label="Photo of the bronze Darvin's statue with a guitar and flower lei"></div></div>

  <h1 class="brand">Sunvale Ride Co</h1>

  <div class="label" style="left:232px;top:225px"><small>Adult</small><span>Single Journey</span></div>
  <div class="price" style="left:434px;top:226px">$20</div>

  <div class="label" style="left:232px;top:300px"><small>Adult</small><span>1 Day</span></div>
  <div class="was" style="left:373px;top:307px">$25</div>
  <div class="price deal" style="left:424px;top:301px">$20</div>
  <div class="tag" style="left:513px;top:309px;width:71px;height:32px">Deal!</div>

  <div class="label" style="left:232px;top:378px"><small>Adult</small><span>2 Days</span></div>
  <div class="price" style="left:434px;top:377px">$30</div>

  <div class="label" style="left:232px;top:458px"><small>Seniors (62+)</small><span>1 Day</span></div>
  <div class="price navy" style="left:434px;top:455px">$20</div>
  <div class="tag" style="left:502px;top:458px;width:120px;height:34px">+1 Day Free</div>

  <div class="label" style="left:674px;top:294px"><small>Children (5-17 years)</small><span>1 Day</span></div>
  <div class="price" style="right:263px;top:296px">$13</div>

  <div class="label" style="left:674px;top:359px"><small>Children (5-17years)</small><span>2 Days</span></div>
  <div class="price" style="right:265px;top:359px">$15</div>

  <div class="label" style="left:670px;top:424px"><small>Children (Under 5 years)</small></div>
  <div class="free" style="right:262px;top:420px">FREE</div>
  <svg style="position:absolute;left:818px;top:458px" width="136" height="16" viewBox="0 0 136 16" aria-hidden="true">
    <path d="M2 8 Q70 6 120 7 Q134 8 130 3" fill="none" stroke="#14186e" stroke-width="1.5"/>
  </svg>

  <a class="book-online" href="#">Book online</a>
</div>
</body>
</html>
```